Re-Design Business Card and Logo for Plastic Printing

Business is a small financial planning (investments, insurance, retirement, etc.) firm. The majority of our clients are 55+ years old, professional occupations (pilots, doctors, bankers, etc.) but not necessarily "high net worth."
I would like to have a design that would be used on clear plastic business cards. I have found a vendor that makes these but I do not have the ability to design these like I want.
I do have one proof but I just don't feel like it's the right one for me. Also, I feel that I need some help with a logo redesign so maybe someone could handle that for me as well.
I want the final design to "eye catching" but still be tasteful. I am open to suggestion regarding colors and such.
I will include the old design as well as the new proof I have to give you an idea of what I current have. Keep in mind, I have no allegiance to the attached designs.
For the second file (Business Card New Proof), the white space shown will be transparent when printed on plastic card.
Target Market(s)
Mostly people age 55+ in professional occupations.
Industry/Entity Type
Financial Service
Contact Information for Business Card
Looking for design that can be printed on clear plastic cards (if possible).
Logo Text
HWC - Harborline Wealth Counsel
Requirements
Must have
- Must be double sided because disclosure is required for compliance reasons.
Designations (must include the Registered trademark symbol as follows)...
MBA, ChFC®, CLU®, CRPS®
Nice to have
- The little icons next to email, phone and fax are nice.
Should not have
- I think I would like to eliminate the Owner and Co-Founder line that you see on the attachments.

```html
<!DOCTYPE html>
<html lang="en">
<head>
<meta charset="utf-8">
<title>Harborline Wealth Counsel – Business Card</title>
<link href="https://fonts.googleapis.com/css2?family=Poppins:ital,wght@0,500;0,600;0,700;1,500&display=swap" rel="stylesheet">
<style>
  :root{
    --backdrop:#e9edf1;
    --card-white:#ffffff;
    --navy-deep:#0c2147;
    --navy-mid:#14306a;
    --brand-navy:#1b3a6e;
    --accent-blue:#2f6fd6;
    --stripe-blue:#2b5fb4;
    --text-light:#f2f5fa;
  }
  *{margin:0;padding:0;box-sizing:border-box}
  html,body{width:984px;height:1200px;overflow:hidden}
  body{background:var(--backdrop);position:relative;font-family:"Poppins",sans-serif}

  .card{position:absolute;left:95px;width:791px;display:flex;box-shadow:0 18px 30px rgba(0,0,0,.18)}
  .card--back{top:63px;height:438px}
  .card--front{top:630px;height:445px}

  .brand-panel{background:var(--card-white);display:flex;flex-direction:column;align-items:center;justify-content:center;gap:10px}
  .card--back .brand-panel{width:254px}
  .card--front .brand-panel{width:257px}
  .brand-mark{width:26px;height:26px;background:var(--brand-navy)}
  .brand-name{color:var(--brand-navy);font-weight:700;font-size:19px;line-height:1.15;text-align:center;text-transform:uppercase;letter-spacing:.5px}

  .info-panel{flex:1;position:relative;overflow:hidden;
    background:radial-gradient(ellipse at 40% 40%,var(--navy-mid) 0%,var(--navy-deep) 85%);color:var(--text-light)}
  .stripes{position:absolute;inset:0}

  .disclosure{position:absolute;left:56px;width:444px;top:196px;font-size:11.3px;font-weight:600;line-height:14.6px;text-align:center;letter-spacing:.3px}

  .tagline{position:absolute;top:60px;left:0;right:0;text-align:center;font-style:italic;font-weight:500;font-size:11.5px;color:var(--accent-blue)}
  .holder-name{position:absolute;left:84px;top:150px;font-weight:700;font-size:17px;letter-spacing:.4px}
  .name-rule{position:absolute;left:84px;top:180px;width:382px;height:4px;background:var(--stripe-blue);opacity:.8}
  .address{position:absolute;left:90px;top:196px;font-style:normal;font-weight:600;font-size:11.5px;line-height:14.7px;letter-spacing:.4px}

  .contacts{position:absolute;left:294px;top:305px;list-style:none}
  .contacts li{display:flex;align-items:center;gap:6px;height:31.5px;font-weight:600;font-size:11.8px;letter-spacing:.3px}
  .contacts svg{width:30px;height:28px;flex:none}
</style>
</head>
<body>

<section class="card card--back">
  <div class="brand-panel">
    <span class="brand-mark"></span>
    <p class="brand-name">Harborline<br>Wealth Counsel</p>
  </div>
  <div class="info-panel">
    <svg class="stripes" viewBox="0 0 537 438" preserveAspectRatio="none">
      <polygon points="0,12 255,0 215,0 0,38" fill="var(--stripe-blue)" opacity=".75"/>
      <polygon points="0,58 255,0 278,0 0,82" fill="var(--stripe-blue)" opacity=".6"/>
      <polygon points="537,392 537,408 410,438 370,438" fill="var(--stripe-blue)" opacity=".7"/>
    </svg>
    <p class="disclosure">Martin Caldwell is a registered representative of and offers securities and advisory services through Northgate Securities Corporation, Member NSIC. Northgate Securities Corporation is member of the Northgate Financial Group which is the marketing name for Northgate National Corporation and its affiliates.</p>
  </div>
</section>

<section class="card card--front">
  <div class="brand-panel">
    <span class="brand-mark"></span>
    <p class="brand-name">Harborline<br>Wealth Counsel</p>
  </div>
  <div class="info-panel">
    <p class="tagline">“ Where the Solutions Become Clear ”</p>
    <h1 class="holder-name">Martin Caldwell,MBA, ChFC®,CLU®,CRPS®</h1>
    <div class="name-rule"></div>
    <address class="address">2817 Tidewater Ave<br>Suite 310<br>Norfolk, VA 23510</address>
    <ul class="contacts">
      <li>
        <svg viewBox="0 0 30 28"><rect x="2" y="0" width="26" height="28" rx="4" fill="var(--stripe-blue)"/><path d="M11 5c-2 1-3 3-2 7s4 9 7 11c2 1 4 0 5-1l-3-4-2 1c-2-2-4-5-4-8l2-1-3-5z" fill="var(--navy-deep)"/></svg>
        <span>(757)555-0148</span>
      </li>
      <li>
        <svg viewBox="0 0 30 28"><rect x="1" y="5" width="28" height="19" fill="var(--stripe-blue)"/><path d="M1 5l14 11L29 5M1 24l10-9M29 24L19 15" stroke="var(--navy-deep)" stroke-width="2" fill="none"/></svg>
        <span>mcaldwell@harborlinewc.com</span>
      </li>
      <li>
        <svg viewBox="0 0 30 28"><rect x="8" y="2" width="14" height="8" fill="none" stroke="var(--stripe-blue)" stroke-width="2"/><rect x="2" y="10" width="26" height="11" rx="3" fill="var(--stripe-blue)"/><rect x="8" y="17" width="14" height="9" fill="var(--navy-deep)" stroke="var(--stripe-blue)" stroke-width="2"/></svg>
        <span>Toll Free (757)555-0193</span>
      </li>
    </ul>
  </div>
</section>

</body>
</html>
```